R. Vantello needs an original business card for property investment professionals

The business card would be to present me as an investor in the real estate business. The market are developers of real estate projects, or other people who would like to sell and also to give us a name as a company. For style, colour and imagery I would like something artistic from Vantello (the artist) with a different touch.

Address, email, cel phone,
Updates

Hi¡ Update¡ I;d like it to stop providing Bright Ledger as a Design and focus in R.Vantello.

Target Market(s)

Real Estate Developer/Investor

Industry/Entity Type

Real Estate

Colors
33a6d7
886aae
e3daeb
cadf82
f78f20

```html
<!DOCTYPE html>
<html lang="en">
<head>
<meta charset="utf-8">
<title>R.Vantello business card</title>
<link href="https://fonts.googleapis.com/css2?family=Arimo:wght@400;700&display=swap" rel="stylesheet">
<style>
  :root {
    --page-bg: #ffffff;
    --card-front: #e2ddd6;
    --card-front-light: #ebe7e1;
    --ink-brown: #5a4430;
    --ink-dark: #141414;
    --ink-blue: #2f3552;
    --band-tint: rgba(255, 250, 235, 0.5);
    --bronze: #a07a45;
    --bronze-dark: #6b4f2c;
    --sand: #e8d9bd;
    --stone: #b9b5ae;
  }
  * { margin: 0; padding: 0; box-sizing: border-box; }
  html, body {
    width: 1200px;
    height: 418px;
    overflow: hidden;
    background: var(--page-bg);
    font-family: "Arimo", Arial, sans-serif;
  }
  .canvas {
    position: relative;
    width: 1200px;
    height: 418px;
  }
  .card {
    position: absolute;
    top: 36px;
    width: 510px;
    height: 336px;
    overflow: hidden;
  }
  .card--front {
    left: 72px;
    background: linear-gradient(135deg, var(--card-front-light), var(--card-front));
  }
  .card--back { left: 638px; }

  .wordmark {
    font-family: "Arimo", Arial, sans-serif;
    font-weight: 700;
    color: var(--ink-brown);
    letter-spacing: 1px;
    line-height: 1;
  }
  .card--front .wordmark {
    position: absolute;
    left: 12px;
    top: 38px;
    font-size: 42px;
  }
  .holder {
    position: absolute;
    left: 282px;
    top: 102px;
    color: var(--ink-dark);
  }
  .holder__name { font-size: 26px; font-weight: 700; line-height: 1.1; }
  .holder__role { font-size: 19px; line-height: 1.3; }
  .contact {
    position: absolute;
    left: 286px;
    top: 228px;
    list-style: none;
    font-size: 17px;
    line-height: 24px;
    color: var(--ink-dark);
    letter-spacing: 0.5px;
  }
  .diagonal-art {
    position: absolute;
    left: 0;
    top: 0;
  }
  .back-art {
    position: absolute;
    inset: 0;
    background:
      linear-gradient(160deg, rgba(255,255,255,0.35) 0%, transparent 40%),
      linear-gradient(100deg, var(--bronze) 0%, var(--sand) 35%, var(--bronze) 60%, var(--stone) 85%, #8f8a83 100%);
  }
  .title-band {
    position: absolute;
    left: 43px;
    top: 120px;
    width: 420px;
    height: 102px;
    background: var(--band-tint);
  }
  .card--back .wordmark {
    position: absolute;
    left: 76px;
    top: 14px;
    font-size: 44px;
  }
  .tagline {
    position: absolute;
    left: 77px;
    top: 68px;
    font-size: 19px;
    color: var(--ink-blue);
  }
</style>
</head>
<body>
<main class="canvas">
  <section class="card card--front">
    <svg class="diagonal-art" width="510" height="336" viewBox="0 0 510 336" role="img" aria-label="Angular bronze and cream artwork band">
      <defs>
        <linearGradient id="bandFill" x1="0" y1="0" x2="1" y2="1">
          <stop offset="0" stop-color="#7a5a34"/>
          <stop offset="0.45" stop-color="#e6d9c3"/>
          <stop offset="0.75" stop-color="#9c7748"/>
          <stop offset="1" stop-color="#d8ccb8"/>
        </linearGradient>
      </defs>
      <polygon points="0,112 264,336 190,336 0,178" fill="url(#bandFill)" stroke="#3a2a18" stroke-width="1"/>
    </svg>
    <div class="wordmark">R.VANTELLO</div>
    <div class="holder">
      <p class="holder__name">John Doe</p>
      <p class="holder__role">broker</p>
    </div>
    <ul class="contact">
      <li>adress:123 xxxxxxxxxx</li>
      <li>phone:123 456 890</li>
      <li>e-mail: info@r.vant.com</li>
    </ul>
  </section>

  <section class="card card--back">
    <div class="back-art" role="img" aria-label="Angular bronze, cream and grey artwork background"></div>
    <div class="title-band">
      <div class="wordmark">R.VANTELLO</div>
      <p class="tagline">real estate developer/investor</p>
    </div>
  </section>
</main>
</body>
</html>
```